Salon and Spa Distributor Business Card

Need a business card. We are are distributor in the salon and spa industry. We identify with natural beauty. Need a card with:
Company Name: Petal Haven"
Title: "President & CEO"
Address
Company Phone number
email
website
Tag Line:" Natural Care for Every Salon"

Industry/Entity Type

Business

Contact Information for Business Card

Name: Lena Morcott
Title: "President & CEO"
Address: 317 Birchfield Ln, Oakvane, NJ 07481
Company Phone number: 800-463-9152
email: lenamorcott@petalhaven-example.com
website: www.petalhaven-example.com

Requirements
Should not have
• No black backgrounds

```html
<!DOCTYPE html>
<html lang="en">
<head>
<meta charset="utf-8">
<title>Petal Haven – Business Card</title>
<link rel="stylesheet" href="https://fonts.googleapis.com/css2?family=Questrial&display=swap">
<style>
  :root {
    --stage: #ece9e4;
    --card-white: #ffffff;
    --brand-green: #17803d;
    --leaf-green: #6abf45;
    --ink: #4a4a4a;
    --ink-dark: #3a3a3a;
    --shadow: rgba(0, 0, 0, 0.18);
  }
  * { box-sizing: border-box; margin: 0; padding: 0; }
  html, body {
    width: 1200px;
    height: 1000px;
    overflow: hidden;
    background: var(--stage);
    font-family: "Questrial", "Century Gothic", sans-serif;
  }
  .canvas {
    position: relative;
    width: 1200px;
    height: 1000px;
  }
  .card {
    position: absolute;
    border-radius: 22px;
    box-shadow: 0 6px 18px var(--shadow);
    overflow: hidden;
  }

  /* Front card */
  .card--front {
    left: 180px;
    top: 160px;
    width: 580px;
    height: 320px;
    background: var(--card-white);
  }
  .front-brand {
    position: absolute;
    left: 44px;
    top: 0;
    height: 100%;
    display: flex;
    align-items: center;
    gap: 12px;
    color: var(--leaf-green);
    font-size: 30px;
  }
  .brand-dot {
    width: 22px;
    height: 22px;
    border-radius: 50%;
    background: var(--leaf-green);
    flex: none;
  }
  .front-details {
    position: absolute;
    right: 36px;
    top: 50px;
    width: 260px;
    text-align: center;
    color: var(--ink);
  }
  .tagline {
    color: var(--leaf-green);
    font-size: 15px;
    letter-spacing: 0.3px;
    white-space: nowrap;
  }
  .company {
    font-size: 22px;
    color: var(--ink);
    margin-top: 2px;
  }
  .person {
    margin-top: 26px;
    font-size: 22px;
    font-weight: 700;
    color: var(--ink-dark);
  }
  .person .surname { color: var(--leaf-green); }
  .role {
    font-size: 17px;
    margin-top: 2px;
  }
  .contact {
    margin-top: 26px;
    font-size: 14px;
    line-height: 1.25;
    white-space: nowrap;
  }

  /* Back card */
  .card--back {
    left: 417px;
    top: 503px;
    width: 516px;
    height: 294px;
    background: var(--brand-green);
    color: var(--card-white);
  }
  .back-brand {
    position: absolute;
    left: 120px;
    top: 105px;
    height: 56px;
    display: flex;
    align-items: center;
    gap: 40px;
    font-size: 38px;
  }
  .back-brand .brand-dot {
    width: 56px;
    height: 56px;
    background: var(--card-white);
  }
  .address {
    position: absolute;
    left: 0;
    right: 0;
    bottom: 28px;
    text-align: center;
    font-size: 14px;
    letter-spacing: 0.4px;
  }
</style>
</head>
<body>
<main class="canvas">
  <section class="card card--front" aria-label="Business card front">
    <div class="front-brand">
      <span class="brand-dot"></span>
      <span class="brand-name">Petal Haven</span>
    </div>
    <div class="front-details">
      <p class="tagline">“Natural Care for Every Salon”</p>
      <p class="company">Petal Haven</p>
      <p class="person">Lena <span class="surname">Morcott</span></p>
      <p class="role">President &amp; CEO</p>
      <div class="contact">
        <p>800 - 463 - 9152</p>
        <p>lenamorcott@petalhaven-example.com</p>
        <p>www.petalhaven-example.com</p>
      </div>
    </div>
  </section>

  <section class="card card--back" aria-label="Business card back">
    <div class="back-brand">
      <span class="brand-dot"></span>
      <span class="brand-name">Petal Haven</span>
    </div>
    <p class="address">317 Birchfield Ln, Oakvane, NJ 07481</p>
  </section>
</main>
</body>
</html>
```